Freelance business trainer needs a new business card

My business is called Tbrite. I provide training in the workplace on management, coaching and mentoring, and customer service topics for a variety of businesses, colleges and private training providers, and teach on management programs. I need a professional but eye catching business card. Business colours grey and orange. My name Linda Marchbank; Tel 07853 416207; email lmarchbank@tbrite.co.uk; website www.tbrite.co.uk.
Happy to have some sort of logo on front and details on back or all on one side
Target Market(s)
SME businesses and colleges - workshops i run are for adults in the workplace
Industry/Entity Type
Training
Look and feel

```html
<!DOCTYPE html>
<html lang="en">
<head>
<meta charset="utf-8">
<title>Tbrite – Business Card</title>
<link rel="stylesheet" href="https://fonts.googleapis.com/css2?family=Ubuntu:wght@500;700&family=Roboto+Condensed:wght@400;500&display=swap">
<style>
  :root {
    --orange: #e3761b;
    --grey-text: #6d6e70;
    --ink: #1d1d1d;
    --rule: #4a4a4a;
    --card-light: #fbfbfa;
    --card-shade: #e9e8e4;
    --backdrop: #eceef2;
  }
  * { margin: 0; padding: 0; box-sizing: border-box; }
  html, body {
    width: 1200px;
    height: 800px;
    overflow: hidden;
    background: var(--backdrop);
  }
  .canvas {
    position: relative;
    width: 1200px;
    height: 800px;
  }
  .card {
    position: absolute;
    left: 100px;
    top: 114px;
    width: 1000px;
    height: 572px;
    background: linear-gradient(165deg, var(--card-light) 0%, #f4f3f1 45%, var(--card-shade) 100%);
    box-shadow: 0 6px 18px rgba(0, 0, 0, 0.12);
    overflow: hidden;
  }
  .accent-bar {
    position: absolute;
    width: 44px;
    background: var(--orange);
  }
  .accent-bar--top-right { top: 0; right: 14px; height: 122px; }
  .accent-bar--bottom-left { bottom: 0; left: 0; height: 150px; }

  .brand {
    position: absolute;
    left: 66px;
    top: 88px;
  }
  .brand__name {
    font-family: "Ubuntu", sans-serif;
    font-weight: 500;
    font-size: 84px;
    line-height: 1;
    color: var(--grey-text);
    letter-spacing: 1px;
  }

  .person {
    position: absolute;
    left: 466px;
    top: 238px;
    right: 0;
  }
  .person__name {
    font-family: "Ubuntu", sans-serif;
    font-weight: 700;
    font-size: 36px;
    color: var(--orange);
    letter-spacing: 0.5px;
  }
  .person__title {
    font-family: "Roboto Condensed", sans-serif;
    font-weight: 500;
    font-size: 27px;
    color: var(--ink);
    margin-top: 4px;
    padding-bottom: 14px;
    border-bottom: 1.5px solid var(--rule);
  }

  .contacts {
    position: absolute;
    left: 490px;
    top: 352px;
    list-style: none;
  }
  .contacts__item {
    display: flex;
    align-items: center;
    gap: 18px;
    height: 48px;
    font-family: "Roboto Condensed", sans-serif;
    font-size: 28px;
    color: var(--ink);
    letter-spacing: 0.3px;
  }
  .contacts__icon {
    width: 28px;
    height: 28px;
    fill: var(--orange);
    flex: none;
  }
</style>
</head>
<body>
<div class="canvas">
  <div class="card">
    <div class="accent-bar accent-bar--top-right"></div>
    <div class="accent-bar accent-bar--bottom-left"></div>

    <div class="brand">
      <span class="brand__name">Tbrite</span>
    </div>

    <div class="person">
      <h1 class="person__name">Linda Marchbank</h1>
      <p class="person__title">Senior Education Consultant</p>
    </div>

    <ul class="contacts">
      <li class="contacts__item">
        <svg class="contacts__icon" viewBox="0 0 28 28" aria-hidden="true">
          <path d="M3 9c0-3 4-5 11-5s11 2 11 5v2h-6V9c-1-1-3-1.5-5-1.5S10 8 9 9v2H3z"/>
          <path d="M7 12h14l3 12H4z"/>
        </svg>
        <span>07853 416207</span>
      </li>
      <li class="contacts__item">
        <svg class="contacts__icon" viewBox="0 0 28 28" aria-hidden="true">
          <path d="M2 7h24v15H2z"/>
          <path d="M2 7l12 9 12-9" fill="none" stroke="#f4f3f1" stroke-width="2"/>
        </svg>
        <span>lmarchbank@tbrite.co.uk</span>
      </li>
      <li class="contacts__item">
        <svg class="contacts__icon" viewBox="0 0 28 28" aria-hidden="true">
          <circle cx="14" cy="14" r="11"/>
          <g fill="none" stroke="#f4f3f1" stroke-width="1.6">
            <ellipse cx="14" cy="14" rx="5" ry="11"/>
            <line x1="3" y1="14" x2="25" y2="14"/>
            <line x1="14" y1="3" x2="14" y2="25"/>
          </g>
        </svg>
        <span>www.tbrite.co.uk</span>
      </li>
    </ul>
  </div>
</div>
</body>
</html>
```